Online trading school - Website design

We are building an online trading school (trading of shares, commodities, indices, currencies). The purpose is to teach online traders how to trade successfully. We need to design the homepage of the website and logo (bramwelloq.com will be the domain). The homepage will contain the following elements

- logo
- Sign in and Register links/buttons
- upper menu
- short introduction
- a couple of bullet points 'Why to join our school?'
- sign up form
- text
- bottom menu

Attached is a draft for the designer. The draft is just for an inspiration, the actual structure of the website can be different if the designer thinks so.

The designer is free to choose colors.

School

3 page

```html
<!DOCTYPE html>
<html lang="en">
<head>
<meta charset="utf-8">
<title>Trading School – Home</title>
<link href="https://fonts.googleapis.com/css2?family=Oswald:wght@400;500&family=Roboto+Condensed:wght@700&family=Open+Sans:wght@400;700&display=swap" rel="stylesheet">
<style>
  :root{
    --blue:#2a56b8;
    --red:#d0163a;
    --amber:#e47a10;
    --purple:#a21c9c;
    --orange:#f0672a;
    --teal:#5aa9c2;
    --navy:#1f2a5c;
    --submit:#2f80c0;
    --ink:#2b2b2b;
    --body:#555;
    --white:#fff;
  }
  *{box-sizing:border-box;margin:0;padding:0}
  html,body{width:1200px;height:1165px;overflow:hidden;background:var(--white)}
  body{position:relative;font-family:"Open Sans",sans-serif}
  .hero{position:absolute;left:0;top:0;width:1200px;height:876px;
    background:radial-gradient(ellipse at 30% 40%,#8a7a64 0%,#5a4d40 40%,#3a3430 75%),#4a403a;}
  .hero-photo{position:absolute;inset:0;
    background:linear-gradient(180deg,rgba(160,150,140,.35) 0%,rgba(60,55,50,.2) 50%,rgba(40,60,30,.45) 100%),
    radial-gradient(ellipse at 25% 35%,rgba(220,190,140,.45) 0%,transparent 45%),
    radial-gradient(ellipse at 45% 78%,rgba(210,210,215,.45) 0%,transparent 35%);}
  .logo{position:absolute;left:74px;top:30px;font-family:"Oswald",sans-serif;font-weight:500;font-size:26px;color:var(--white)}
  .auth{position:absolute;top:53px;height:34px;width:93px;border-radius:5px 5px 0 0;color:var(--white);
    font-weight:700;font-size:13px;display:flex;align-items:center;justify-content:center}
  .auth.signin{left:916px;background:var(--red)}
  .auth.register{left:1013px;background:var(--amber)}
  .main-nav{position:absolute;left:75px;top:86px;width:1050px;height:49px;background:var(--blue);border-radius:6px;
    display:flex;align-items:center;padding-left:30px}
  .main-nav a{font-family:"Roboto Condensed",sans-serif;font-weight:700;font-size:17px;color:var(--white);text-decoration:none;margin-right:42px}
  .social{position:absolute;right:12px;display:flex;gap:8px;font-size:11px;font-weight:700;color:var(--white)}
  .intro{position:absolute;left:458px;top:216px;width:640px;color:var(--white)}
  .intro h1{font-family:"Oswald",sans-serif;font-weight:400;font-size:31px;line-height:1.2;margin-bottom:8px}
  .intro p{font-size:16.5px;line-height:26px}
  .why{position:absolute;left:74px;top:556px;width:129px;height:245px;background:var(--teal);border-radius:4px}
  .why h2{font-family:"Oswald",sans-serif;font-weight:400;font-size:30px;line-height:31px;color:var(--white);text-align:center;margin-top:36px}
  .card{position:absolute;top:702px;width:129px;height:99px;background:var(--white);border-radius:4px;
    font-family:"Roboto Condensed",sans-serif;font-weight:700;font-size:17.5px;line-height:20px;color:var(--navy);
    text-align:center;padding:24px 6px 0}
  .card svg{position:absolute;left:55px;top:-11px}
  .join{position:absolute;left:772px;top:437px;width:350px}
  .join-banner{position:absolute;left:0;top:0}
  .join-banner span{position:absolute;left:0;top:33px;width:350px;text-align:center;font-family:"Oswald",sans-serif;
    font-size:30px;color:var(--white)}
  .join-form{position:absolute;left:8px;top:80px;width:332px;height:284px;background:var(--orange);border-radius:0 0 4px 4px;padding:32px 18px 0}
  .field{display:block;width:296px;height:40px;background:var(--white);border:0;margin-bottom:10px;padding-left:13px;
    font-family:"Open Sans",sans-serif;font-size:15px;color:#555;display:flex;align-items:center}
  .agree{display:flex;align-items:center;gap:10px;color:var(--white);font-size:14px;margin-top:16px;padding-left:4px}
  .agree i{width:10px;height:10px;background:var(--white)}
  .submit{position:absolute;left:77px;top:219px;width:179px;height:44px;border-radius:22px;background:var(--submit);border:2px solid var(--white);
    color:var(--white);font-weight:700;font-size:18px;letter-spacing:1px;display:flex;align-items:center;justify-content:center}
  .offer{position:absolute;left:74px;top:908px;width:1060px}
  .offer h2{font-family:"Oswald",sans-serif;font-weight:400;font-size:30px;color:var(--ink);margin-bottom:10px}
  .offer p{font-size:15.2px;line-height:26px;color:var(--body)}
  .footer{position:absolute;left:0;top:1112px;width:1200px;height:53px;background:var(--blue);color:var(--white);
    font-size:14.5px;display:flex;align-items:center;padding-left:73px}
  .footer .social{right:75px}
</style>
</head>
<body>
  <section class="hero">
    <div class="hero-photo" role="img" aria-label="Photo of a smiling woman working on a laptop in a bright café"></div>
    <div class="logo">LOGO HERE</div>
    <a class="auth signin">SIGN IN</a>
    <a class="auth register">REGISTER</a>
    <nav class="main-nav">
      <a>HOME</a><a>ABOUT OUR SCHOOL</a><a>RISK WARNING</a><a>FAQ</a><a>TRADING GLOSSARY</a><a>CONTACT</a>
      <div class="social"><span>Friendly</span><span>Chirper</span><span>Circles</span></div>
    </nav>
    <div class="intro">
      <h1>WELCOME TO SCHOOL NAME</h1>
      <p>Lorem ipsum dolor sit amet, consectetur adipiscing elit, sed do eiusmod tempor incididunt ut labore et dolore magna aliqua. Ut enim ad minim veniam, quis nostrud exercitation ullamco laboris nisi ut aliquip ex ea commodo consequat. Lorem ipsum dolor sit amet, consectetur adipiscing elit, sed do eiusmod tempor incididunt.</p>
    </div>
    <div class="why"><h2>WHY TO<br>JOIN US?</h2></div>
    <div class="card" style="left:74px"><svg width="18" height="22"><path d="M0 0H18V22L9 15L0 22Z" fill="#1f2a5c"/></svg>Best trading tips ever</div>
    <div class="card" style="left:210px"><svg width="18" height="22"><path d="M0 0H18V22L9 15L0 22Z" fill="#1f2a5c"/></svg>Secret tips from experts</div>
    <div class="card" style="left:346px"><svg width="18" height="22"><path d="M0 0H18V22L9 15L0 22Z" fill="#1f2a5c"/></svg>We teach you how to trade online</div>
    <div class="card" style="left:483px"><svg width="18" height="22"><path d="M0 0H18V22L9 15L0 22Z" fill="#1f2a5c"/></svg>Learn how to trade commodities</div>
    <div class="card" style="left:618px"><svg width="18" height="22"><path d="M0 0H18V22L9 15L0 22Z" fill="#1f2a5c"/></svg>Learn how to become a trader</div>
    <div class="join">
      <div class="join-form">
        <div class="field">First name</div>
        <div class="field">Last name</div>
        <div class="field">Email</div>
        <div class="agree"><i></i>Agree with our tems and conditions</div>
        <div class="submit">SUBMIT</div>
      </div>
      <div class="join-banner">
        <svg width="350" height="98"><path d="M2 16L175 0L348 16L346 72L175 97L4 84Z" fill="#a21c9c"/></svg>
        <span>JOIN OUR SCHOOL NOW!</span>
      </div>
    </div>
  </section>
  <section class="offer">
    <h2>WHAT DO WE OFFER?</h2>
    <p>Sed ut perspiciatis unde omnis iste natus error sit voluptatem accusantium doloremque laudantium, totam rem aperiam, eaque ipsa quae ab illo inventore veritatis et quasi architecto beatae vitae dicta sunt explicabo. Nemo enim ipsam voluptatem quia voluptas sit aspernatur aut odit aut fugit, sed quia consequuntur magni dolores eos qui ratione voluptatem sequi nesciunt. Neque porro quisquam est, qui dolorem ipsum quia dolor sit amet, consectetur, adipisci velit, sed quia non numquam eius modi tempora incidunt ut labore et dolore magnam aliquam quaerat voluptatem. Sed ut perspiciatis unde omnis iste natus error sit voluptatem accusantium doloremque laudantium.</p>
  </section>
  <footer class="footer">
    2016 © Brightpath Tutors. &nbsp;|&nbsp; Terms and Conditions &nbsp;|&nbsp; Privacy Protection
    <div class="social"><span>Friendly</span><span>Chirper</span><span>Circles</span></div>
  </footer>
</body>
</html>
```